Need an awesome Modern Facebook and Twitter cover page

We are looking for a redesign for our facebook and twitter cover to coincide with our new design.

```html
<!DOCTYPE html>
<html lang="en">
<head>
<meta charset="utf-8">
<title>KeyShellIT – Social Covers</title>
<link rel="stylesheet" href="https://fonts.googleapis.com/css2?family=IBM+Plex+Mono:wght@700&family=Montserrat:wght@500&family=Open+Sans:wght@600;700&display=swap">
<style>
  :root {
    --page-bg: #eef6fd;
    --brand-blue: #2a8fd8;
    --ink: #151515;
    --panel-black: #0d0d0d;
    --white: #ffffff;
    --photo-light: #e9ecef;
    --photo-mid: #c9cfd6;
    --photo-warm: #d9d2c8;
    --photo-cool: #6f8fa8;
  }
  * { margin: 0; padding: 0; box-sizing: border-box; }
  html, body {
    width: 1200px; height: 1200px; overflow: hidden;
    background: var(--page-bg);
  }
  .sheet { position: relative; width: 1200px; height: 1200px; }
  .sheet-label {
    position: absolute; left: 0; width: 1200px; text-align: center;
    font-family: "Montserrat", sans-serif; font-weight: 500;
    font-size: 42px; letter-spacing: 2px; color: var(--brand-blue);
    line-height: 1;
  }
  .sheet-label--facebook { top: 68px; }
  .sheet-label--twitter { top: 1103px; }
  .cover {
    position: absolute; display: block;
    box-shadow: 0 3px 6px rgba(0,0,0,0.28);
  }
  .cover--facebook { left: 70px; top: 177px; width: 1060px; height: 392px; }
  .cover--twitter { left: 40px; top: 650px; width: 1120px; height: 374px; }
  .brand-name { font-family: "Open Sans", sans-serif; font-weight: 700; fill: var(--brand-blue); letter-spacing: -2px; }
  .headline { font-family: "IBM Plex Mono", monospace; font-weight: 700; fill: var(--ink); }
  .headline--accent { fill: var(--brand-blue); }
  .tagline { font-family: "Open Sans", sans-serif; font-weight: 600; fill: #222; }
  .site-url { font-family: "Open Sans", sans-serif; font-weight: 700; fill: var(--white); }
</style>
</head>
<body>
<main class="sheet">
  <h2 class="sheet-label sheet-label--facebook">FACEBOOK COVER</h2>

  <svg class="cover cover--facebook" viewBox="0 0 1325 490" xmlns="http://www.w3.org/2000/svg">
    <defs>
      <linearGradient id="fbLeftPhoto" x1="0" y1="0" x2="1" y2="1">
        <stop offset="0" stop-color="var(--photo-light)"/>
        <stop offset="0.5" stop-color="#f4f5f6"/>
        <stop offset="1" stop-color="var(--photo-mid)"/>
      </linearGradient>
      <linearGradient id="fbTeamPhoto" x1="0" y1="0" x2="1" y2="1">
        <stop offset="0" stop-color="var(--photo-warm)"/>
        <stop offset="0.45" stop-color="#eeeeea"/>
        <stop offset="0.75" stop-color="var(--photo-cool)"/>
        <stop offset="1" stop-color="#c7ccd1"/>
      </linearGradient>
    </defs>
    <g class="left-panel" role="img" aria-label="Faded greyscale photo of an office team at work">
      <rect width="572" height="490" fill="url(#fbLeftPhoto)"/>
      <rect width="572" height="490" fill="#ffffff" opacity="0.55"/>
    </g>
    <rect class="dark-panel" x="572" width="753" height="490" fill="var(--panel-black)"/>
    <rect class="divider" x="570" width="5" height="490" fill="var(--brand-blue)"/>
    <polygon points="425,150 1165,40 725,620" fill="none" stroke="var(--white)" stroke-width="44" stroke-linejoin="round"/>
    <polygon points="425,150 1165,40 725,620" fill="var(--brand-blue)" stroke="var(--brand-blue)" stroke-width="24" stroke-linejoin="round"/>
    <g role="img" aria-label="Photo of smiling young professionals working at laptops and computers in an office">
      <polygon points="448,158 1140,56 727,598" fill="url(#fbTeamPhoto)" stroke="url(#fbTeamPhoto)" stroke-width="8" stroke-linejoin="round"/>
    </g>
    <text class="brand-name" x="34" y="110" font-size="66">KeyShellIT</text>
    <text class="headline" x="42" y="188" font-size="44">NOW SERCHING</text>
    <text class="headline" x="42" y="237" font-size="44">IN THE WRONG</text>
    <rect x="215" y="216" width="164" height="3" fill="var(--brand-blue)"/>
    <text class="headline headline--accent" x="42" y="286" font-size="44">RIGHT PLACE</text>
    <text class="tagline" x="43" y="367" font-size="20.5">our platform provides quick commandline and</text>
    <text class="tagline" x="43" y="393" font-size="20.5">GUI demonstrations that are essential to the</text>
    <text class="tagline" x="43" y="420" font-size="20.5">everyday life of IT Professionals</text>
    <g class="globe-icon" fill="none" stroke="var(--brand-blue)" stroke-width="1.8">
      <circle cx="1081" cy="440" r="10"/>
      <ellipse cx="1081" cy="440" rx="4.5" ry="10"/>
      <line x1="1071" y1="440" x2="1091" y2="440"/>
      <line x1="1073" y1="434" x2="1089" y2="434"/>
      <line x1="1073" y1="446" x2="1089" y2="446"/>
    </g>
    <text class="site-url" x="1100" y="447" font-size="22">keyshellit.com</text>
  </svg>

  <svg class="cover cover--twitter" viewBox="0 0 1400 467" xmlns="http://www.w3.org/2000/svg">
    <defs>
      <linearGradient id="twLeftPhoto" x1="0" y1="0" x2="1" y2="1">
        <stop offset="0" stop-color="var(--photo-light)"/>
        <stop offset="0.5" stop-color="#f4f5f6"/>
        <stop offset="1" stop-color="var(--photo-mid)"/>
      </linearGradient>
      <linearGradient id="twTeamPhoto" x1="0" y1="0" x2="1" y2="1">
        <stop offset="0" stop-color="var(--photo-warm)"/>
        <stop offset="0.45" stop-color="#eeeeea"/>
        <stop offset="0.75" stop-color="var(--photo-cool)"/>
        <stop offset="1" stop-color="#c7ccd1"/>
      </linearGradient>
    </defs>
    <g class="left-panel" role="img" aria-label="Faded greyscale photo of an office team at work">
      <rect width="655" height="467" fill="url(#twLeftPhoto)"/>
      <rect width="655" height="467" fill="#ffffff" opacity="0.55"/>
    </g>
    <rect class="dark-panel" x="655" width="745" height="467" fill="var(--panel-black)"/>
    <rect class="divider" x="653" width="5" height="467" fill="var(--brand-blue)"/>
    <polygon points="512,128 1232,30 770,600" fill="none" stroke="var(--white)" stroke-width="44" stroke-linejoin="round"/>
    <polygon points="512,128 1232,30 770,600" fill="var(--brand-blue)" stroke="var(--brand-blue)" stroke-width="24" stroke-linejoin="round"/>
    <g role="img" aria-label="Photo of smiling young professionals working at laptops and computers in an office">
      <polygon points="535,137 1207,46 772,578" fill="url(#twTeamPhoto)" stroke="url(#twTeamPhoto)" stroke-width="8" stroke-linejoin="round"/>
    </g>
    <text class="brand-name" x="70" y="126" font-size="78">KeyShellIT</text>
    <text class="headline" x="70" y="187" font-size="47">NOW SERCHING</text>
    <text class="headline" x="70" y="237" font-size="47">IN THE WRONG</text>
    <rect x="253" y="215" width="170" height="3" fill="var(--brand-blue)"/>
    <text class="headline headline--accent" x="70" y="288" font-size="47">RIGHT PLACE</text>
    <text class="tagline" x="72" y="329" font-size="20.5">our platform provides quick commandline and</text>
    <text class="tagline" x="72" y="354" font-size="20.5">GUI demonstrations that are essential to the</text>
    <text class="tagline" x="72" y="380" font-size="20.5">everyday life of IT Professionals</text>
    <g class="globe-icon" fill="none" stroke="var(--brand-blue)" stroke-width="1.8">
      <circle cx="1170" cy="364" r="10"/>
      <ellipse cx="1170" cy="364" rx="4.5" ry="10"/>
      <line x1="1160" y1="364" x2="1180" y2="364"/>
      <line x1="1162" y1="358" x2="1178" y2="358"/>
      <line x1="1162" y1="370" x2="1178" y2="370"/>
    </g>
    <text class="site-url" x="1189" y="371" font-size="22">keyshellit.com</text>
  </svg>

  <h2 class="sheet-label sheet-label--twitter">TWITTER COVER</h2>
</main>
</body>
</html>
```